Cozy Sprouts Business Cards

I need a business card for my new Company called Cozy Sprouts. We create handmade baby moccasins, headbands, t-shirts and more. I want some that will appeal to parents, and to go with the colors of my logo that I have attached. feel free to be creative. I would like my logo placed somewhere on the card.

Industry/Entity Type

Retail

Contact Information for Business Card

Cozy Sprouts
24816 Maplecrest D #5172
Irvine Ca 92738
Rosalind Vantrey Ceo
Info@Cozy-Sprouts.com
www.Cozy-Sprouts.com
Phone 9495817320

Requirements
Nice to have
• Logo included

```html
<!DOCTYPE html>
<html lang="en">
<head>
<meta charset="utf-8">
<title>Cozy Sprouts Business Cards</title>
<link href="https://fonts.googleapis.com/css2?family=Comic+Neue:wght@400;700&family=Lora:wght@500;600&display=swap" rel="stylesheet">
<style>
  :root {
    --stage: #e6e3e0;
    --card: #ffffff;
    --ink: #111111;
    --accent: #e07a45;
    --shadow: rgba(40, 30, 25, 0.22);
  }
  * { box-sizing: border-box; margin: 0; padding: 0; }
  html, body { width: 1200px; height: 768px; overflow: hidden; }
  body { background: var(--stage); position: relative; }

  .card {
    position: absolute;
    top: 229px;
    width: 520px;
    height: 310px;
    background: var(--card);
    box-shadow: 0 10px 26px var(--shadow);
  }
  .card--front { left: 50px; }
  .card--back { left: 630px; }

  .brand {
    font-family: "Comic Neue", "Comic Sans MS", cursive;
    font-weight: 400;
    color: var(--ink);
    display: flex;
    flex-direction: column;
    align-items: center;
  }
  .brand__mark {
    background: var(--accent);
    border-radius: 6px;
  }

  .card--front .brand {
    position: absolute;
    left: 0; right: 0; top: 72px;
  }
  .card--front .brand__mark { width: 56px; height: 56px; margin-bottom: 22px; }
  .card--front .brand__name { font-size: 50px; line-height: 1; }

  .card--back .brand {
    position: absolute;
    right: 28px; bottom: 26px;
  }
  .card--back .brand__mark { width: 62px; height: 62px; margin-bottom: 14px; }
  .card--back .brand__name { font-size: 36px; line-height: 1; }

  .person {
    position: absolute;
    left: 30px; top: 26px;
  }
  .person__name {
    font-family: "Comic Neue", "Comic Sans MS", cursive;
    font-weight: 700;
    font-size: 21px;
    color: var(--accent);
  }
  .person__title {
    font-family: Arial, Helvetica, sans-serif;
    font-size: 10px;
    color: var(--ink);
    margin-top: 1px;
  }

  .contact {
    position: absolute;
    left: 30px; top: 142px;
    font-family: "Lora", Georgia, serif;
    font-weight: 600;
    font-size: 13px;
    line-height: 1.45;
    color: var(--ink);
    list-style: none;
  }
  .contact__address { margin-bottom: 10px; }
  .contact__row { display: flex; align-items: center; gap: 8px; }
  .contact__icon { width: 11px; height: 11px; fill: var(--accent); flex: none; }
</style>
</head>
<body>
  <section class="card card--front" aria-label="Card front">
    <div class="brand">
      <div class="brand__mark"></div>
      <div class="brand__name">Cozy Sprouts</div>
    </div>
  </section>

  <section class="card card--back" aria-label="Card back">
    <div class="person">
      <div class="person__name">Rosalind Vantrey</div>
      <div class="person__title">CEO</div>
    </div>

    <ul class="contact">
      <li class="contact__address">24816 Maplecrest D #5172<br>Irvine Ca 92738</li>
      <li class="contact__row">
        <svg class="contact__icon" viewBox="0 0 12 12" aria-hidden="true"><path d="M1 3.5C1 2 2.5 1 6 1s5 1 5 2.5v1H8.5V3.3H3.5v1.2H1z M2.5 6l1.5-1.5h4L9.5 6v4.5h-7z"/></svg>
        <span>9495817320</span>
      </li>
      <li class="contact__row">
        <svg class="contact__icon" viewBox="0 0 12 12" aria-hidden="true"><path d="M0.5 2h11v8h-11z M1.5 3l4.5 3.5L10.5 3z" fill-rule="evenodd"/></svg>
        <span>Info@Cozy-Sprouts.com</span>
      </li>
      <li class="contact__row">
        <svg class="contact__icon" viewBox="0 0 12 12" aria-hidden="true"><circle cx="6" cy="6" r="5.5"/><path d="M0.8 5.4h10.4v1.2H0.8z M5.4 0.6h1.2v10.8H5.4z" fill="#fff"/></svg>
        <span>www.Cozy-Sprouts.com</span>
      </li>
    </ul>

    <div class="brand">
      <div class="brand__mark"></div>
      <div class="brand__name">Cozy Sprouts</div>
    </div>
  </section>
</body>
</html>
```